Design home page for quorvant.xyz

We’re seeking a sleek, lead-generation-focused single-page website for Quorvant.xyz that communicates our expertise in delivering high-intent leads to mid-sized businesses. The goal is to guide visitors toward scheduling a free consultation while emphasizing our performance-based approach and comprehensive service offerings.

Industry/Entity Type

Marketing

Number of Pages Required

1 page

Font styles to use
Sans Serif

Requirements
Must have
• content from https://pages.tillowmark.com/doc/d/7hRtWqLMPZX402KDNe19sbYQ3Vb8FkwTtPa6Ue2kHLSF/view?tab=t.0
Nice to have
• color pallet from here https://pages.tillowmark.com/doc/d/9kwebRA4-ZQTofCVyLpHmn52bPWJ83gdX5fjroarr7T/view?tab=t.0

```html
<!DOCTYPE html>
<html lang="en">
<head>
<meta charset="utf-8">
<title>Quorvant.xyz — Home</title>
<link href="https://fonts.googleapis.com/css2?family=Outfit:wght@300;400;500;600;700&display=swap" rel="stylesheet">
<style>
:root{
  --red:#a30f1b;
  --red-deep:#8f0c17;
  --cream:#faf1dc;
  --cream-soft:#fbf5e6;
  --ink:#1d1d1d;
  --muted:#555;
  --dark:#2b2b2b;
  --stage:#bdbdbd;
  --orange:#f7941d;
  --white:#fff;
  --line:#e6d9d9;
}
*{box-sizing:border-box;margin:0;padding:0}
html,body{width:849px;height:1200px;overflow:hidden;background:var(--stage)}
body{font-family:"Outfit",sans-serif;color:var(--ink)}
.board{position:absolute;left:0;top:0;width:1624px;height:2296px;transform:scale(0.52278);transform-origin:0 0}
.abs{position:absolute}
.page{position:absolute;width:655px;overflow:hidden}
.band{position:absolute;left:0;width:655px}
.center{text-align:center}
.h2{font-size:20px;font-weight:600;color:var(--ink)}
.h2 .accent{color:var(--red)}
.swoosh{height:3px;border-radius:3px;background:var(--red)}
.lead{font-size:11px;line-height:15px;color:#333}
.small{font-size:7px;line-height:10px;color:#555}
.card{position:absolute;background:var(--white);border:1px solid var(--line);border-radius:3px;box-shadow:0 4px 12px rgba(163,15,27,.08)}
.card.is-red{background:var(--red);border-color:var(--red);color:#fff}
.card-title{font-size:10px;font-weight:600;line-height:13px}
.icon-ring{position:absolute;border-radius:50%;background:#fff;display:flex;align-items:center;justify-content:center}
.btn{position:absolute;display:flex;align-items:center;justify-content:center;gap:6px;font-weight:500;color:#fff;border-radius:2px}
</style>
</head>
<body>
<div class="board">

<!-- LEFT PAGE -->
<section class="page" style="left:124px;top:62px;height:2143px;background:#fff">

  <!-- Hero -->
  <div class="band hero" style="top:0;height:381px;background:var(--cream)">
    <div class="abs" style="left:65px;top:24px;font-size:20px;font-weight:600">quorvant.xyz</div>
    <h1 class="abs" style="left:65px;top:86px;font-size:21px;font-weight:500;line-height:25px">High-Intent Leads Delivered<br><span style="color:var(--red)">Directly to Your Pipeline</span></h1>
    <p class="abs" style="left:65px;top:148px;width:222px;font-size:9px;line-height:13.5px">Take the guesswork out of lead generation. We connect you with high-intent prospects who are genuinely interested in what you offer, helping you grow your sales pipeline with ease.</p>
    <p class="abs" style="left:65px;top:216px;width:222px;font-size:9.5px;line-height:13px;font-weight:600">Let’s talk about how we can deliver the leads your business needs.</p>
    <div class="btn" style="left:65px;top:270px;width:257px;height:39px;background:var(--red);font-size:13.5px">Schedule a Free Call Today
      <svg width="13" height="10" viewBox="0 0 13 10"><path d="M0 5h11M7 1l4 4-4 4" stroke="#fff" stroke-width="1.6" fill="none"/></svg></div>
    <div class="abs" role="img" aria-label="Line illustration of a sales funnel with megaphone, gears, light bulb and coins" style="left:340px;top:70px;width:270px;height:250px;border-radius:8px;background:radial-gradient(circle at 50% 45%,#f3e1d6 0%,#f6ead8 55%,var(--cream) 100%)"></div>
  </div>

  <!-- Results -->
  <div class="band" style="top:381px;height:379px;background:#fff">
    <div class="abs" style="left:20px;top:80px;width:615px;height:260px;background-image:linear-gradient(#f1eded 1px,transparent 1px),linear-gradient(90deg,#f1eded 1px,transparent 1px);background-size:22px 22px;opacity:.7"></div>
    <h2 class="h2 abs center" style="left:0;width:655px;top:38px">We Deliver Results, <span class="accent">Not Promises</span></h2>
    <div class="swoosh abs" style="left:283px;top:70px;width:98px"></div>
    <p class="lead abs center" style="left:120px;width:420px;top:86px">At Quorvant.xyz, we specialize in providing conversion-ready leads that fuel sustainable business growth.</p>

    <div class="card is-red" style="left:69px;top:163px;width:154px;height:157px;padding:22px 24px">
      <svg width="38" height="30" viewBox="0 0 38 30" fill="none" stroke="#fff" stroke-width="1.4"><path d="M14 4H7a9 9 0 0 0 0 18h7M14 9H7a4 4 0 0 0 0 8h7"/><rect x="14" y="3" width="5" height="7"/><rect x="14" y="16" width="5" height="7"/><circle cx="29" cy="6" r="3"/><circle cx="29" cy="21" r="3"/><path d="M24 14h9M24 28h9"/></svg>
      <div class="card-title" style="margin-top:15px">Entrepreneur-<br>Led Expertise</div>
      <p class="small" style="color:#fbe3e3;margin-top:10px">Founded by seasoned entrepreneurs with proven lead generation success.</p>
    </div>
    <div class="card" style="left:252px;top:163px;width:154px;height:157px;padding:22px 24px">
      <svg width="38" height="30" viewBox="0 0 38 30" fill="none" stroke="var(--red)" stroke-width="1.4"><rect x="2" y="2" width="30" height="20" rx="1"/><path d="M2 7h30M8 12h6M8 16h6"/><path d="M20 13v12l3-3 3 5 2-1-3-5h4z"/></svg>
      <div class="card-title" style="margin-top:15px">Comprehensive<br>Approach</div>
      <p class="small" style="margin-top:10px">From SEO to PPC campaigns and high-value content creation, we manage it all.</p>
    </div>
    <div class="card" style="left:436px;top:163px;width:154px;height:157px;padding:22px 24px">
      <svg width="38" height="32" viewBox="0 0 38 32" fill="none" stroke="var(--red)" stroke-width="1.4"><path d="M4 20V14M10 20V10M16 20V12M22 20V6M28 20V3"/><path d="M3 11l8-6 6 4 10-7"/><circle cx="18" cy="26" r="4"/></svg>
      <div class="card-title" style="margin-top:15px">Performance-Based<br>Model</div>
      <p class="small" style="margin-top:10px">No upfront costs—we succeed only when you do.</p>
    </div>
  </div>

  <!-- End-to-End -->
  <div class="band" style="top:760px;height:505px;background:var(--red);color:#fff">
    <h2 class="abs center" style="left:0;width:655px;top:36px;font-size:19px;font-weight:600;line-height:19px">Comprehensive End-to-End<br>Lead Generation</h2>
    <div class="abs" style="left:276px;top:86px;width:98px;height:3px;border-radius:3px;background:#fff"></div>
    <p class="abs center" style="left:130px;width:395px;top:102px;font-size:10.5px;line-height:15px">We handle everything needed to deliver high-quality leads so you can focus on scaling your business.</p>

    <svg class="abs" style="left:234px;top:170px" width="200" height="200" viewBox="0 0 200 200" fill="none" stroke="#fff" stroke-width="1.2">
      <path d="M43 67 A86 86 0 1 0 162 67"/><circle cx="43" cy="67" r="2.5" fill="var(--red)"/><circle cx="162" cy="67" r="2.5" fill="var(--red)"/>
      <circle cx="100" cy="183" r="2.5" fill="var(--red)"/><circle cx="15" cy="108" r="2.5" fill="var(--red)"/><circle cx="185" cy="108" r="2.5" fill="var(--red)"/>
    </svg>
    <div class="abs" style="left:264px;top:187px;width:140px;height:140px;border-radius:50%;background:radial-gradient(circle,#fbf0d0 0%,#f2e2b6 100%);display:flex;align-items:center;justify-content:center;color:var(--ink);font-size:15px;font-weight:600">quorvant.xyz</div>

    <div class="icon-ring" style="left:199px;top:170px;width:44px;height:44px;background:transparent;border:1.3px solid #fff"><svg width="22" height="18" viewBox="0 0 22 18" fill="none" stroke="#fff" stroke-width="1.2"><rect x="1" y="1" width="20" height="16"/><path d="M4 5h14M4 9h8M4 13h8"/></svg></div>
    <div class="abs" style="left:40px;top:176px;width:140px;text-align:right"><div style="font-size:10px;font-weight:600">Content Creation</div><p style="font-size:6.5px;line-height:9.5px;margin-top:3px">High-value gated content, articles, and blog posts to attract and convert leads.</p></div>

    <div class="icon-ring" style="left:428px;top:170px;width:44px;height:44px;background:transparent;border:1.3px solid #fff"><svg width="22" height="20" viewBox="0 0 22 20" fill="none" stroke="#fff" stroke-width="1.2"><rect x="1" y="3" width="14" height="12"/><path d="M15 8l5-4v12l-5-4"/></svg></div>
    <div class="abs" style="left:491px;top:173px;width:140px"><div style="font-size:10px;font-weight:600">PPC Campaigns</div><p style="font-size:6.5px;line-height:9.5px;margin-top:3px">Targeted paid search to drive qualified leads.</p></div>

    <div class="icon-ring" style="left:200px;top:288px;width:44px;height:44px;background:transparent;border:1.3px solid #fff"><svg width="22" height="20" viewBox="0 0 22 20" fill="none" stroke="#fff" stroke-width="1.2"><rect x="1" y="1" width="20" height="13"/><path d="M7 18h8M11 14v4M5 5h12M5 9h7"/></svg></div>
    <div class="abs" style="left:40px;top:291px;width:139px;text-align:right"><div style="font-size:10px;font-weight:600">Design &amp; Development</div><p style="font-size:6.5px;line-height:9.5px;margin-top:3px">Professional assets and optimized landing pages for maximum engagement.</p></div>

    <div class="icon-ring" style="left:429px;top:284px;width:44px;height:44px;background:transparent;border:1.3px solid #fff"><svg width="22" height="22" viewBox="0 0 22 22" fill="none" stroke="#fff" stroke-width="1.2"><circle cx="11" cy="11" r="6"/><circle cx="11" cy="11" r="2"/><path d="M11 1v3M11 18v3M1 11h3M18 11h3M4 4l2 2M16 16l2 2M4 18l2-2M16 6l2-2"/></svg></div>
    <div class="abs" style="left:489px;top:288px;width:140px"><div style="font-size:10px;font-weight:600">Real-Time Optimization</div><p style="font-size:6.5px;line-height:9.5px;margin-top:3px">Ongoing analysis and adjustments for peak performance and ROI.</p></div>

    <div class="icon-ring" style="left:314px;top:362px;width:44px;height:44px;background:transparent;border:1.3px solid #fff"><svg width="24" height="18" viewBox="0 0 24 18" fill="none" stroke="#fff" stroke-width="1.2"><rect x="2" y="1" width="20" height="12" rx="2"/><path d="M9 17h6M12 13v4"/><text x="12" y="10" font-size="6" fill="#fff" stroke="none" text-anchor="middle" font-family="Outfit">SEO</text></svg></div>
    <div class="abs center" style="left:236px;top:424px;width:200px"><div style="font-size:10px;font-weight:600">SEO &amp; Social Media</div><p style="font-size:6.5px;line-height:9.5px;margin-top:3px">Organic strategies to attract quality traffic and generate leads.</p></div>
  </div>

  <!-- Why choose -->
  <div class="band" style="top:1265px;height:455px;background:#fff">
    <h2 class="abs" style="left:78px;top:48px;font-size:20px;font-weight:600;line-height:24px">Why Choose<br><span style="color:var(--red)">Quorvant.xyz?</span></h2>
    <div class="swoosh abs" style="left:78px;top:97px;width:98px"></div>
    <p class="lead abs" style="left:288px;top:56px;width:300px">We specialize in delivering high-intent leads that drive measurable growth. Here’s how we stand out:</p>

    <div class="abs" role="img" aria-label="Photo of a smiling professional holding a tablet, framed in a red circle" style="left:70px;top:148px;width:215px;height:230px;border-radius:50%;background:radial-gradient(circle at 60% 40%,#c0182a 0%,#a30f1b 55%,#d9c8c2 100%)"></div>
    <div class="abs" style="left:52px;top:198px;width:72px;height:48px;background:#fff;border:1px solid #eee;box-shadow:0 3px 8px rgba(0,0,0,.1)"></div>
    <div class="abs center" style="left:214px;top:310px;width:72px;height:64px;background:#fff;box-shadow:0 4px 10px rgba(0,0,0,.12);padding-top:10px;font-size:7px;font-weight:600;color:var(--red)">
      <svg width="18" height="18" viewBox="0 0 18 18" fill="none" stroke="var(--red)" stroke-width="1.2"><circle cx="5" cy="4" r="2"/><circle cx="13" cy="4" r="2"/><path d="M2 8h14l-5 5v4H7v-4z"/></svg><br>HIGH-INTENT<br>LEADS</div>

    <svg class="abs" style="left:275px;top:170px" width="100" height="210" viewBox="0 0 100 210" fill="none" stroke="var(--red)" stroke-width="1.3">
      <path d="M0 97 H40 V30 Q40 20 50 20 H95"/><path d="M0 97 H95"/><path d="M40 97 V170 Q40 180 50 180 H95"/>
    </svg>
    <div class="icon-ring" style="left:369px;top:174px;width:52px;height:52px;box-shadow:0 3px 10px rgba(163,15,27,.15)"><svg width="24" height="22" viewBox="0 0 24 22" fill="none" stroke="var(--red)" stroke-width="1.2"><path d="M3 20v-4M8 20v-7M13 20v-5M18 20v-10"/><path d="M2 11l6-5 5 3 8-7"/></svg></div>
    <div class="abs" style="left:435px;top:156px;width:165px"><div style="font-size:11px;font-weight:600">Results-Driven Approach</div><p class="small" style="margin-top:5px">We handle all aspects of lead generation, from creating lead magnets to executing advertising and SEO campaigns, delivering high-quality leads that align with your goals.</p></div>

    <div class="icon-ring" style="left:369px;top:268px;width:52px;height:52px;box-shadow:0 3px 10px rgba(163,15,27,.15)"><svg width="22" height="22" viewBox="0 0 22 22" fill="none" stroke="var(--red)" stroke-width="1.2"><path d="M6 20v-4a7 7 0 1 1 10-7l2 4h-2v4h-4v3"/><circle cx="11" cy="9" r="2.5"/></svg></div>
    <div class="abs" style="left:435px;top:250px;width:165px"><div style="font-size:11px;font-weight:600">Tailored Strategies</div><p class="small" style="margin-top:5px">Our campaigns are designed to connect you with prospects who are genuinely interested in the type of products or services you offer.</p></div>

    <div class="icon-ring" style="left:369px;top:362px;width:52px;height:52px;box-shadow:0 3px 10px rgba(163,15,27,.15)"><svg width="24" height="22" viewBox="0 0 24 22" fill="none" stroke="var(--red)" stroke-width="1.2"><circle cx="7" cy="15" r="5"/><circle cx="17" cy="15" r="5"/><path d="M12 2v8M9 5l3-3 3 3"/></svg></div>
    <div class="abs" style="left:435px;top:344px;width:165px"><div style="font-size:11px;font-weight:600">Simplified Growth Solutions</div><p class="small" style="margin-top:5px">With all the heavy lifting managed by our team, you can focus entirely on growing your business and closing more deals.</p></div>
  </div>

  <!-- Tailored content -->
  <div class="band" style="top:1720px;height:423px;background:var(--dark);color:#fff">
    <h2 class="abs center" style="left:0;width:655px;top:48px;font-size:18px;font-weight:500">Tailored Content for High-Intent Lead Capture</h2>
    <p class="abs center" style="left:0;width:655px;top:90px;font-size:10px">We create custom-crafted content tailored for your audience:</p>
    <div class="abs" style="left:246px;top:150px;width:174px;height:75px;background:var(--red)"></div>
    <div class="abs" style="left:72px;top:224px;width:522px;height:1px;background:#666"></div>
    <div class="abs" style="left:72px;top:301px;width:522px;height:1px;background:#666"></div>
    <div class="abs" style="left:245px;top:150px;width:1px;height:226px;background:#666"></div>
    <div class="abs" style="left:420px;top:150px;width:1px;height:226px;background:#666"></div>

    <svg width="0" height="0" style="position:absolute"><defs>
      <symbol id="doc" viewBox="0 0 18 20"><rect x="2" y="1" width="14" height="18" rx="1.5" fill="none" stroke="#fff" stroke-width="1.5"/><path d="M5 6h8M5 10h8M5 14h5" stroke="#fff" stroke-width="1.5"/></symbol>
    </defs></svg>
    <div class="abs" style="left:100px;top:175px;display:flex;gap:14px;align-items:center;font-size:10px;line-height:13px"><svg width="18" height="20"><use href="#doc"/></svg>Guides and<br>eBooks</div>
    <div class="abs" style="left:274px;top:175px;display:flex;gap:14px;align-items:center;font-size:10px;line-height:13px"><svg width="20" height="20" viewBox="0 0 20 20"><rect x="1" y="1" width="18" height="18" rx="2" fill="#fff"/><path d="M5 15v-3M9 15v-5M13 15v-7" stroke="var(--red)" stroke-width="1.8"/></svg>Industry<br>Insights Reports</div>
    <div class="abs" style="left:458px;top:175px;display:flex;gap:14px;align-items:center;font-size:10px;line-height:13px"><svg width="20" height="20" viewBox="0 0 20 20"><path d="M10 10V1a9 9 0 1 1-9 9z" fill="#fff"/><path d="M12 8V1a7 7 0 0 1 7 7z" fill="#fff"/></svg>Infographics &amp;<br>Visual Guides</div>
    <div class="abs" style="left:98px;top:250px;display:flex;gap:14px;align-items:center;font-size:10px;line-height:13px"><svg width="20" height="22"><use href="#doc"/></svg>Glossary of<br>Industry Terms</div>
    <div class="abs" style="left:276px;top:250px;display:flex;gap:14px;align-items:center;font-size:10px;line-height:13px"><svg width="18" height="22"><use href="#doc"/></svg>Checklist for<br>Best Practices</div>
    <div class="abs" style="left:460px;top:250px;display:flex;gap:14px;align-items:center;font-size:10px;line-height:13px"><svg width="20" height="20" viewBox="0 0 20 20"><rect x="1" y="2" width="18" height="16" rx="2" fill="none" stroke="#fff" stroke-width="1.5"/><path d="M4 14l4-4 3 2 5-5" stroke="#fff" stroke-width="1.5" fill="none"/></svg>Trend Spotting<br>Forecast</div>
    <div class="abs" style="left:96px;top:328px;display:flex;gap:14px;align-items:center;font-size:10px;line-height:13px"><svg width="20" height="20" viewBox="0 0 20 20"><rect x="1" y="1" width="18" height="18" rx="2" fill="none" stroke="#fff" stroke-width="1.5"/><path d="M1 6h18M5 10h10M5 14h4" stroke="#fff" stroke-width="1.5"/></svg>Templates and<br>Toolkits</div>
    <div class="abs" style="left:274px;top:328px;display:flex;gap:14px;align-items:center;font-size:10px;line-height:13px"><svg width="22" height="20" viewBox="0 0 22 20"><rect x="2" y="7" width="16" height="11" rx="2" fill="#fff"/><circle cx="10" cy="12" r="3" fill="var(--dark)"/><path d="M13 2v6M13 2h6l-2 2 2 2h-6" stroke="#fff" stroke-width="1.3" fill="#fff"/></svg>Competitive<br>Landscape</div>
    <div class="abs" style="left:462px;top:334px;display:flex;gap:14px;align-items:center;font-size:10px"><svg width="18" height="20"><use href="#doc"/></svg>Whitepapers</div>
  </div>
</section>

<!-- RIGHT PAGE -->
<section class="page" style="left:843px;top:60px;height:2035px;background:#fff">

  <!-- Process -->
  <div class="band" style="top:0;height:376px;background:var(--cream-soft)">
    <h2 class="h2 abs center" style="left:0;width:655px;top:40px;font-size:18px">How We Deliver <span class="accent">High-Quality Leads</span></h2>
    <div class="swoosh abs" style="left:320px;top:66px;width:90px"></div>
    <p class="abs center" style="left:0;width:655px;top:84px;font-size:10px">Our streamlined process ensures you receive ready-to-engage leads without the hassle:</p>
    <svg class="abs" style="left:150px;top:170px" width="370" height="140" viewBox="0 0 370 140" fill="none" stroke="var(--red)" stroke-width="1" stroke-dasharray="2 3">
      <path d="M0 18 C40 20 60 60 110 65 C140 70 150 90 170 108"/><path d="M205 110 C240 100 240 70 290 60 C320 55 330 40 360 18"/>
    </svg>
    <div class="abs center" style="left:104px;top:166px;width:44px;height:44px;border-radius:50%;background:var(--red);color:#fff;font-size:16px;font-weight:600;line-height:44px;box-shadow:0 0 0 5px #fff">1</div>
    <div class="abs center" style="left:306px;top:256px;width:44px;height:44px;border-radius:50%;background:var(--red);color:#fff;font-size:16px;font-weight:600;line-height:44px;box-shadow:0 0 0 5px #fff">2</div>
    <div class="abs center" style="left:516px;top:166px;width:44px;height:44px;border-radius:50%;background:var(--red);color:#fff;font-size:16px;font-weight:600;line-height:44px;box-shadow:0 0 0 5px #fff">3</div>
    <div class="abs center" style="left:56px;top:230px;width:140px"><div style="font-size:9.5px;font-weight:600;line-height:12px">Precise Market<br>Targeting</div><p class="small" style="margin-top:10px">We start by understanding your ideal customer profile and identifying high-intent prospects in your market.</p></div>
    <div class="abs center" style="left:258px;top:134px;width:140px"><div style="font-size:9.5px;font-weight:600;line-height:12px">Customized<br>Campaign Execution</div><p class="small" style="margin-top:9px">We take the time to understand your audience, creating and running campaigns tailored to their interests, leveraging insights from advertising, SEO, and lead magnets.</p></div>
    <div class="abs center" style="left:466px;top:230px;width:144px"><div style="font-size:9.5px;font-weight:600;line-height:12px">All-Inclusive<br>Management</div><p class="small" style="margin-top:10px">From strategy to execution, we handle every detail, delivering leads while you focus on closing deals.</p></div>
  </div>

  <!-- Apart -->
  <div class="band" style="top:376px;height:361px;background:#fff">
    <h2 class="abs" style="left:70px;top:44px;font-size:18px;font-weight:600;line-height:19px">What Sets Us<br><span style="color:var(--red)">Apart?</span></h2>
    <div class="swoosh abs" style="left:70px;top:88px;width:72px"></div>
    <p class="abs" style="left:251px;top:46px;width:330px;font-size:10.5px;line-height:15px">We’re more than just a lead generation service—our approach ensures valuable opportunities for your business:</p>

    <div class="card" style="left:65px;top:158px;width:153px;height:149px;padding:42px 20px"><div class="card-title" style="font-weight:500">High-Intent Leads</div><p class="small" style="margin-top:18px;line-height:12px">The high-intent leads we generate provide a solid starting point for building meaningful connections</p></div>
    <div class="card is-red" style="left:254px;top:160px;width:153px;height:148px;padding:42px 22px"><div class="card-title">Complete Service</div><p class="small" style="color:#fbe3e3;margin-top:11px;line-height:12px">We take care of everything needed to generate leads, so you can stay focused on growing your business.</p></div>
    <div class="card" style="left:446px;top:159px;width:153px;height:149px;padding:42px 20px"><div class="card-title" style="font-weight:500">Success-Based<br>Partnership</div><p class="small" style="margin-top:9px;line-height:12px">With our results-driven model, you pay only for the leads we deliver, ensuring value every step of the way.</p></div>
    <div class="icon-ring" style="left:96px;top:138px;width:46px;height:46px;border:3px solid var(--red);border-bottom-color:#fff;border-left-color:#fff"><svg width="22" height="18" viewBox="0 0 22 18" fill="none" stroke="var(--red)" stroke-width="1.2"><path d="M2 4h14M2 9h18M2 14h14M13 1l3 3-3 3M17 6l3 3-3 3"/></svg></div>
    <div class="icon-ring" style="left:283px;top:140px;width:46px;height:46px;border:3px solid #777;border-bottom-color:#fff;border-left-color:#fff"><svg width="22" height="22" viewBox="0 0 22 22" fill="none" stroke="var(--red)" stroke-width="1.2"><circle cx="11" cy="11" r="7"/><circle cx="11" cy="11" r="3"/><path d="M11 1v3M11 18v3M1 11h3M18 11h3"/></svg></div>
    <div class="icon-ring" style="left:476px;top:138px;width:46px;height:46px;border:3px solid var(--red);border-bottom-color:#fff;border-left-color:#fff"><svg width="24" height="18" viewBox="0 0 24 18" fill="none" stroke="var(--red)" stroke-width="1.2"><path d="M1 6l5-4 5 3 5-3 6 4-8 9z"/><path d="M8 9l3 3M11 7l3 3"/></svg></div>
  </div>

  <!-- Effortless growth -->
  <div class="band" style="top:737px;height:470px;background:var(--cream-soft)">
    <h2 class="abs" style="left:159px;top:42px;font-size:18px;font-weight:500;display:flex;align-items:center;gap:6px">Effortless Growth, <span style="background:var(--red);color:#fff;padding:2px 6px;border-radius:2px">Designed for You</span></h2>
    <div class="swoosh abs" style="left:277px;top:77px;width:72px"></div>
    <p class="abs center" style="left:0;width:655px;top:94px;font-size:11px">We simplify lead generation, so you can focus on growing your business:</p>

    <div class="card" style="left:67px;top:143px;width:248px;height:268px;border-color:#eee">
      <div class="center" style="margin-top:26px;font-size:12.5px;font-weight:500">Hands-Off Convenience</div>
      <p class="small center" style="margin:8px 18px 0;font-size:7.5px;line-height:11px">We manage the strategy, content, advertising, and optimization, delivering a steady flow of high-quality prospects.</p>
      <svg class="abs" style="left:0;top:108px" width="248" height="140" viewBox="0 0 248 140">
        <path d="M120 15V110M52 50V40H188V50M76 110V98H160V110" stroke="#333" stroke-width="1" fill="none"/>
        <rect x="80" y="2" width="80" height="18" rx="9" fill="#fff" stroke="#eee"/>
        <text x="120" y="14" font-size="7.5" font-weight="600" text-anchor="middle" font-family="Outfit">quorvant.xyz</text>
        <rect x="22" y="52" width="62" height="14" rx="7" fill="#2b2b2b"/><text x="53" y="62" font-size="6.5" fill="#fff" text-anchor="middle" font-family="Outfit">Strategy</text>
        <rect x="158" y="52" width="62" height="14" rx="7" fill="var(--red)"/><text x="189" y="62" font-size="6.5" fill="#fff" text-anchor="middle" font-family="Outfit">Content</text>
        <rect x="44" y="111" width="66" height="14" rx="7" fill="var(--red)"/><text x="77" y="121" font-size="6.5" fill="#fff" text-anchor="middle" font-family="Outfit">Optimization</text>
        <rect x="128" y="111" width="66" height="14" rx="7" fill="#2b2b2b"/><text x="161" y="121" font-size="6.5" fill="#fff" text-anchor="middle" font-family="Outfit">Advertising</text>
      </svg>
    </div>
    <div class="card is-red" style="left:344px;top:143px;width:249px;height:268px">
      <div class="center" style="margin-top:26px;font-size:12.5px;font-weight:500">Built to Scale</div>
      <p class="small center" style="margin:8px 20px 0;font-size:7.5px;line-height:11px;color:#fbe3e3">Our process adapts to your growth goals, ensuring consistent lead flow whether you’re starting small or scaling rapidly.</p>
      <div class="abs" style="left:36px;top:113px;width:182px;height:130px;background:#f3e9d6;border-radius:3px;overflow:hidden">
        <div style="height:10px;background:#fff"></div>
        <svg class="abs" style="left:0;top:0" width="182" height="130" viewBox="0 0 182 130" fill="none" stroke="var(--red)" stroke-width="1"><path d="M50 65V40H108M74 90H124V68"/></svg>
        <div class="abs center" style="left:108px;top:25px;width:60px;height:49px;background:#2b2b2b;color:#fff;font-size:6px;line-height:7px;padding-top:29px;font-weight:600">Consistent<br>Lead Flow</div>
        <div class="abs center" style="left:14px;top:63px;width:60px;height:48px;background:var(--orange);color:#fff;font-size:6px;line-height:7px;padding-top:30px;font-weight:600">Adapt to<br>Growth Goals</div>
      </div>
    </div>
  </div>

  <!-- Stories -->
  <div class="band" style="top:1207px;height:631px;background:#fff">
    <h2 class="h2 abs center" style="left:0;width:655px;top:40px;font-size:18px">Proven Success <span class="accent">Stories</span></h2>
    <div class="swoosh abs" style="left:292px;top:66px;width:72px"></div>
    <p class="abs center" style="left:0;width:655px;top:86px;font-size:10.5px">Discover how our clients have achieved exceptional growth with Quorvant.xyz:</p>

    <div class="card" style="left:61px;top:131px;width:164px;height:162px;padding:12px 22px">
      <div style="color:var(--red);font-size:20px;font-weight:700;line-height:20px">”</div>
      <p class="small" style="margin-top:6px;font-size:7.5px;line-height:12px;color:#333">"Quorvant.xyz has completely transformed our lead generation efforts. We’ve seen a 35% increase in high-quality leads in just three months."</p>
      <div class="abs" style="left:22px;top:126px;font-size:7.5px;font-weight:600">Ravi T.</div>
      <div class="abs" style="left:22px;top:138px;font-size:6px;color:#555">VP of Sales at a Mid-Sized B2B Firm</div>
    </div>
    <div class="card" style="left:246px;top:131px;width:164px;height:162px;padding:12px 22px">
      <div style="color:var(--red);font-size:20px;font-weight:700;line-height:20px">”</div>
      <p class="small" style="margin-top:6px;font-size:7.5px;line-height:12px;color:#333">"The team at Quorvant.xyz took care of everything—from content to campaigns. Their performance-based model meant we only paid when results came in. It’s a win-win!"</p>
      <div class="abs" style="left:22px;top:126px;font-size:7.5px;font-weight:600">Monica E.</div>
      <div class="abs" style="left:22px;top:138px;font-size:6px;color:#555">CEO of a Professional Services Company</div>
    </div>
    <div class="card" style="left:430px;top:131px;width:164px;height:162px;padding:12px 22px">
      <div style="color:var(--red);font-size:20px;font-weight:700;line-height:20px">”</div>
      <p class="small" style="margin-top:6px;font-size:7.5px;line-height:12px;color:#333">"Working with Quorvant.xyz is like having an in-house growth team. Their ability to create and optimize content-driven campaigns helped us double our inbound inquiries."</p>
      <div class="abs" style="left:22px;top:126px;font-size:7.5px;font-weight:600">Peter K.</div>
      <div class="abs" style="left:22px;top:138px;font-size:6px;color:#555">Marketing Director at a SaaS Company</div>
    </div>
  </div>

  <!-- Footer band -->
  <div class="band" style="top:1838px;height:197px;background:var(--dark);color:#fff">
    <div class="abs center" style="left:0;width:655px;top:94px;font-size:18px;font-weight:600">quorvant xyz</div>
    <div class="abs center" style="left:0;width:655px;top:128px;font-size:11px;font-weight:500">Driving Real Growth, One Lead at a Time</div>
    <div class="abs center" style="left:0;width:655px;top:157px;font-size:7px">Copyright 2025 Quorvant.xyz, LLC. All rights reserved.</div>
  </div>

  <!-- CTA card -->
  <div class="abs" style="left:60px;top:1559px;width:534px;height:352px;background:var(--red);color:#fff;border-radius:2px">
    <h2 class="abs center" style="left:0;width:534px;top:36px;font-size:16px;font-weight:500;line-height:19px">Ready to Unlock Scalable Growth<br>for Your Business?</h2>
    <p class="abs center" style="left:0;width:534px;top:94px;font-size:8.5px">Schedule a call to learn how we can help your business grow predictably and efficiently.</p>
    <div class="icon-ring" style="left:90px;top:141px;width:50px;height:50px;border:3px solid #f3d4d4;border-bottom-color:#fff"><svg width="24" height="22" viewBox="0 0 24 22" fill="none" stroke="var(--red)" stroke-width="1.2"><circle cx="6" cy="4" r="2"/><circle cx="12" cy="4" r="2"/><circle cx="18" cy="4" r="2"/><path d="M2 9h20l-7 6v5H9v-5z"/></svg></div>
    <div class="icon-ring" style="left:244px;top:141px;width:50px;height:50px;border:3px solid #f3d4d4;border-bottom-color:#fff"><svg width="24" height="22" viewBox="0 0 24 22" fill="none" stroke="var(--red)" stroke-width="1.2"><path d="M3 9v5h4l8 5V3L7 8H3z"/><path d="M18 7l3-3M19 11h4M18 15l3 3"/></svg></div>
    <div class="icon-ring" style="left:402px;top:141px;width:50px;height:50px;border:3px solid #f3d4d4;border-bottom-color:#fff"><svg width="22" height="22" viewBox="0 0 22 22" fill="none" stroke="var(--red)" stroke-width="1.2"><circle cx="11" cy="10" r="5"/><path d="M9 16h4v3H9zM11 1v3M2 10h3M17 10h3M4 3l2 2M18 3l-2 2"/></svg></div>
    <div class="abs center" style="left:55px;top:204px;width:120px"><div style="font-size:9.5px;font-weight:600">High-Intent Leads</div><p style="font-size:5.5px;line-height:8px;margin-top:5px">Leads that match your ideal customer profile.</p></div>
    <div class="abs center" style="left:209px;top:204px;width:120px"><div style="font-size:9.5px;font-weight:600">Custom Campaigns</div><p style="font-size:5.5px;line-height:8px;margin-top:5px">designed to engage and convert your audience.</p></div>
    <div class="abs center" style="left:367px;top:204px;width:120px"><div style="font-size:9.5px;font-weight:600">Actionable Insights</div><p style="font-size:5.5px;line-height:8px;margin-top:5px">to optimize performance and scale effectively.</p></div>
    <div class="btn" style="left:152px;top:276px;width:233px;height:39px;background:var(--orange);font-size:13px;border-radius:1px">Schedule your call now
      <svg width="13" height="10" viewBox="0 0 13 10"><path d="M0 5h11M7 1l4 4-4 4" stroke="#fff" stroke-width="1.6" fill="none"/></svg></div>
  </div>
</section>

</div>
</body>
</html>
```